Quirky Business Card Design

Business card:
A quirky card for a professional audience

Business:
A professional consultancy offering corporate training and coaching

I've attached my sketches and happy for you to shapen the design and/or add your own ideas.

Front of card (see file 2 below):
Card must be easy for client to find among many
A bit quirky – implies that it needs thought, needs orientation
White card, black high gloss letters

Arrows:
One spot colour – fresh amber-orange, but not fluro nor candy colour
A colour that is not feminine nor masculine; old nor young
Meant to represent the amber of traffic lights
? black outline
Arrows oriented left to right and bottom to top i.e. headed in the right direction
May need to work in a straight line for header or footer or invoices (see file 3 below)

Back of card (e.g. in file 1):
Very clean and easy to read
Preferred fonts: I like the aesthetic of Century Gothic but with “a”.
Copy to include:
Kettle Bloom Co
Marnie Talbot
t: +61 (0)412 307 196
e: marnie@kettlebloomco.com
w: www.kettlebloomco.com

May use the by-line “turning bold plans into action”

I am looking for a web page design in the future so I am looking to be delighted!!

Dear Designers,

I would like the copy at the back of the card to include the registered business number: 

ABN: 8123 604 2917

Many thanks,

Marnie.

Industry/Entity Type

Training

```html
<!DOCTYPE html>
<html lang="en">
<head>
<meta charset="utf-8">
<title>Kettle Bloom Co – Business Card</title>
<link rel="stylesheet" href="https://fonts.googleapis.com/css2?family=Questrial&display=swap">
<style>
  :root {
    --backdrop: #2a2a2a;
    --card-dark: #221f1f;
    --card-light: #ffffff;
    --ink: #1d1b1b;
    --amber: #f37021;
    --paper-text: #ffffff;
  }
  * { margin: 0; padding: 0; box-sizing: border-box; }
  html, body {
    width: 1200px;
    height: 900px;
    overflow: hidden;
    background: var(--backdrop);
    font-family: "Questrial", "Century Gothic", sans-serif;
  }
  .stage {
    position: relative;
    width: 1200px;
    height: 900px;
  }
  .card {
    position: absolute;
    top: 305px;
    width: 500px;
    height: 290px;
    border-radius: 26px;
    overflow: hidden;
  }

  /* Front */
  .card--front {
    left: 60px;
    background: var(--card-dark);
    color: var(--paper-text);
    display: flex;
    flex-direction: column;
    align-items: center;
    justify-content: center;
  }
  .front__name {
    font-size: 52px;
    line-height: 1;
    color: var(--paper-text);
    letter-spacing: -0.5px;
    white-space: nowrap;
  }
  .front__tagline {
    margin-top: 34px;
    font-size: 15px;
    color: var(--amber);
    white-space: nowrap;
  }

  /* Back */
  .card--back {
    left: 640px;
    background: var(--card-light);
    color: var(--ink);
    text-align: center;
  }
  .back__name {
    margin-top: 52px;
    font-size: 44px;
    line-height: 1;
    color: var(--ink);
    white-space: nowrap;
  }
  .back__company {
    margin-top: 36px;
    font-size: 20px;
    line-height: 1.1;
    color: var(--amber);
  }
  .back__person {
    font-size: 16px;
    line-height: 1.2;
    color: var(--ink);
  }
  .contact {
    display: flex;
    justify-content: center;
    margin-top: 16px;
    font-size: 13.5px;
    line-height: 1.35;
    white-space: nowrap;
  }
  .contact__col--left { text-align: right; padding-right: 9px; }
  .contact__col--right { text-align: left; padding-left: 9px; border-left: 2px solid var(--amber); }
  .back__band {
    position: absolute;
    left: 0;
    right: 0;
    bottom: 0;
    height: 16px;
    background: var(--amber);
  }
</style>
</head>
<body>
<main class="stage">
  <section class="card card--front" aria-label="Card front">
    <p class="front__name">Kettle Bloom Co</p>
    <p class="front__tagline">“turning bold plans into action”</p>
  </section>

  <section class="card card--back" aria-label="Card back">
    <p class="back__name">Kettle Bloom Co</p>
    <p class="back__company">Kettle Bloom Co</p>
    <p class="back__person">Marnie Talbot</p>
    <div class="contact">
      <div class="contact__col contact__col--left">
        <p>t: +61 (0)412 307 196</p>
        <p>e: marnie@kettlebloomco.com</p>
      </div>
      <div class="contact__col contact__col--right">
        <p>w: www.kettlebloomco.com</p>
        <p>ABN: 8123 604 2917</p>
      </div>
    </div>
    <div class="back__band"></div>
  </section>
</main>
</body>
</html>
```